Etiketten für Ätherische Öle, Extrakte und Speiseöle gesucht
Zielgruppe
Wir verkaufen natürlich Produkte. Ätherische öle, Extrakte, Speise öle.
Wir verkaufen im Webshop, Kaufrix und auch im Betrieb.
https://www.natur-feyo.com
Wir verkaufen hauptsächlich innerhalb Italiens und Deutschland daher doppel sprachig.
Aufgabenstellung
Guten Tag
Bitte verwenden Sie! : * beispiel_10_ml_etikett_nachbau.jpg *
Da mir die kleinste Größe die wichtigste ist habe ich ein beispiel Hochgeladen. Das kleinste Etikett lässt sich öffnen und daher sind nur 7 cm ersichtlich und man muss das Etikett aufmachen.
Habe ein Beispiel Hochgeladen. Aber bitte einfach kreativ sein. *Anhang: beispiel Etikett*
Sobald ich eine Art vom kelinsten habe würde ich dies für die 2 anderen Größen übernehmen aber das man Sie irgendwie gut unterscheiden kann da dies dann komplett andere Produkte (Extrakte/Speise öl) sein werden.
Erstellung von drei unterschiedlichen Größen von Etiketten mit folgenden Eigenschaften:
Am wichtigsten ist mir das kleinste Etikett da dies auch am schwersten ist daher habe ich die anderen Größen nun gelöscht!
• 10 ml Länge: 155 mm Breite: 32 mm.
Brauche 3 unterschiedliche Grund Farben: z. B. Ätherische Öle (Grün) Extrakte (Rot) Speiseöle (gelb). Die Farben lasse ich sie entscheiden.
Die Etiketten müssen 2 Sprachen (Deutsch / Italienisch) sein deshalb muss dieses berücksichtigt werden.
Anbei finden Sie:
• Logo (Bild Logo)
• Beispiel Text ätherische Öle
• Bilder der aktuellen Flaschen
Unter https://www.natur-feyo.com/de finden Sie meine Seite
Anmerkung: Im Anhang: *Back*
Habe ich mein Logo mit Firmennamen ; Natur des Holmberg Viktor
Da ich jedoch nicht alle Produkte im biologischen Anbau habe und mein Logo zu miss Verständnis führen könnte habe ich ein Bildliches Logo gemacht das ich fortan auf meinen Produkten haben möchte. Im besonderes dieses Grün das in beiden vorhanden ist versuche ich zu integrieren.
Habe selbst ein Etikett designet das aber sehr unprofessionell wirkt aber dieses Grüne das ich gerne als merkmal unterbringen würde.
Siehe Anhang: neemöl

```html
<!DOCTYPE html>
<html lang="de">
<head>
<meta charset="utf-8">
<title>Etikett Lavendel fein</title>
<link href="https://fonts.googleapis.com/css2?family=Arimo:wght@400;700&family=Roboto+Condensed:wght@400&family=Poiret+One&display=swap" rel="stylesheet">
<style>
  :root {
    --ink: #1a1a1a;
    --leaf: #8cc63f;
    --leaf-light: #d8ec8a;
    --leaf-pale: #f1f8cf;
    --band: #5cb84a;
    --frame: #c8c8c8;
    --logo-ink: #444444;
    --petal: #8f86e0;
    --paper: #ffffff;
  }
  html, body { margin: 0; padding: 0; overflow: hidden; background: var(--paper); }
  .label {
    position: relative;
    width: 1200px;
    height: 248px;
    overflow: hidden;
    background: var(--paper);
    font-family: "Arimo", Arial, sans-serif;
    color: var(--ink);
  }
  .artwork {
    position: absolute; left: 0; top: 0; width: 400px; height: 248px;
    background:
      linear-gradient(90deg, rgba(255,255,255,0) 70%, var(--paper) 100%),
      radial-gradient(ellipse 180px 120px at 60px 200px, var(--leaf) 0%, rgba(140,198,63,0) 100%),
      linear-gradient(160deg, var(--leaf-pale) 0%, var(--leaf-light) 55%, var(--leaf) 100%);
  }
  .flower {
    position: absolute; left: 232px; top: 6px; width: 152px; height: 160px;
    border-radius: 50%;
    background: radial-gradient(circle at 50% 48%, #7a3b2e 0%, #c8602e 14%, var(--petal) 34%, rgba(190,180,240,0.7) 62%, rgba(255,255,255,0) 72%);
  }
  .logo-box {
    position: absolute; left: 18px; top: 21px; width: 158px; height: 167px;
    box-sizing: border-box;
    background: var(--paper);
    border: 2px solid var(--frame);
    display: flex; align-items: center; justify-content: center;
  }
  .logo-name {
    font-family: "Roboto Condensed", "Arial Narrow", sans-serif;
    font-size: 16px; color: var(--logo-ink); text-align: center; line-height: 1.3;
  }
  .product-band {
    position: absolute; left: 0; top: 203px; width: 390px; height: 33px;
    background: linear-gradient(90deg, var(--band) 0%, var(--band) 70%, rgba(92,184,74,0) 100%);
  }
  .product-name {
    position: absolute; left: 20px; top: 206px;
    font-family: "Poiret One", sans-serif;
    font-size: 24px; color: var(--paper); letter-spacing: 0.5px;
  }
  .product-name small { font-size: 18px; }
  .info { position: absolute; left: 398px; width: 792px; }
  .usage {
    top: 10px; font-size: 11.2px; line-height: 15.1px; text-align: justify; margin: 0;
  }
  .ingredients { top: 107px; font-size: 14.6px; line-height: 17px; margin: 0; }
  .ingredients-note { top: 127px; font-size: 11.2px; margin: 0; }
  .company { top: 148px; font-size: 11.6px; line-height: 15.2px; font-weight: 700; margin: 0; }
  .batch { top: 202px; font-size: 12.2px; line-height: 15.2px; margin: 0; }
</style>
</head>
<body>
<div class="label">
  <div class="artwork" role="img" aria-label="Hellgrüne geschwungene Blätterfläche als Hintergrund"></div>
  <div class="flower" role="img" aria-label="Aquarell einer violetten Passionsblume"></div>

  <div class="logo-box">
    <div class="logo-name">d. Holmberg Viktor</div>
  </div>

  <div class="product-band"></div>
  <div class="product-name">LAVENDEL <small>FEIN</small></div>

  <p class="info usage"><b>D |</b> 100% natürliches Ätherisches Öl. Aroma-Kosmetikum zur Körperpflege.Anwendung: Als Haut- u. Massageöl max 15 Tr. Mit 50 ml z.B. Mandelöl mischen. Als Badezusatz 8-15 Tr. Auf 4 Eßl. Sahne oder Milch ins Badewasser geben. / Nur in der angegeben Verdünnung anwenden! Nicht in die Augen oder auf die Schleimhäute bringen! Außer Reichweite von Kindern lagern. Abgefüllt in Italien. / <b>IT |</b> 100% olio essenziale naturale. Cosmetico aromatico per la cura del corpo. Modo d'uso: Come olio da massaggio o olio per il corpo: versare max. 15 gocce in 50ml di liquido p.es. olio di mandorla. / Da usare solo diluito come da indicazione! Evitare il contatto con occhi e mucose! Tenere fuori dalla portata die bambini. Imbottigliato in Italy.</p>

  <p class="info ingredients">Inhaltsstoffe / Ingredients: Lavandula angustifolia oil, Limonene*, Linalool*, geraniol*</p>
  <p class="info ingredients-note">*natürliche Bestandteile des ätherischen Öls / * Olio essenziale con sostanze naturali</p>

  <p class="info company">Natur des Holmberg Viktor, Feldweg 14, I-39012 Meran, IVA: IT01938475620, CF.: HLMVKT88C14F132Z<br>
  Tel.: +39 0471/482615 Handy: 3381204967, https://www.natur-feyo.com/, info.naturfeyo@gmail.com</p>

  <p class="info batch">LottoNummer/CH nummer: 123456<br>
  Verfalls Datum: xxxx oder Symbol für 12 Monate nach öffnung</p>
</div>
</body>
</html>
```